Artistically challenged consultant needs a sexy business card.

I need a business card design for my consultancy business. I work primarily in the pacific on international development program focusing on tourism, economic empowerment and training. I would like to use a light blue/green to reference the pacific and also a simple design of a sprouting coconut (photo attached for reference) to reference growth and development.
The business card should have icons for email, phone, skype, ABN and linked in.

```html
<!DOCTYPE html>
<html lang="en">
<head>
<meta charset="utf-8">
<title>Consultant Business Card</title>
<link rel="stylesheet" href="https://fonts.googleapis.com/css2?family=Arimo:wght@400&family=Tinos:wght@400&display=swap">
<style>
  :root {
    --backdrop: #e6e8eb;
    --card: #ffffff;
    --pacific-blue: #3b9bd8;
    --forest-green: #215f2f;
    --ink: #3a3a3a;
    --icon: #3b9bd8;
    --husk: #b09a72;
    --leaf: #8dbb55;
  }
  html, body {
    margin: 0;
    padding: 0;
    width: 1200px;
    height: 801px;
    overflow: hidden;
    background: var(--backdrop);
  }
  .business-card {
    position: absolute;
    left: 150px;
    top: 143px;
    width: 900px;
    height: 514px;
    background: var(--card);
    box-shadow: 0 6px 24px rgba(0, 0, 0, 0.18);
    overflow: hidden;
  }
  .identity {
    position: absolute;
    right: 110px;
    top: 48px;
  }
  .identity__name {
    margin: 0;
    font-family: "Arimo", Arial, sans-serif;
    font-weight: 400;
    font-size: 36px;
    letter-spacing: 0.5px;
    color: var(--pacific-blue);
  }
  .identity__title {
    margin: 4px 0 0 26px;
    font-family: "Arimo", Arial, sans-serif;
    font-size: 20px;
    color: var(--ink);
    word-spacing: 14px;
  }
  .sprouting-coconut {
    position: absolute;
    right: 50px;
    top: 160px;
    width: 170px;
    height: 238px;
    border-radius: 10px 10px 0 0;
    background: linear-gradient(to bottom, var(--leaf) 0%, #b8cf8f 45%, #c8b894 62%, var(--husk) 100%);
  }
  .accent-line {
    position: absolute;
    left: 0;
    right: 0;
    top: 398px;
    height: 6px;
    background: var(--pacific-blue);
  }
  .footer-band {
    position: absolute;
    left: 0;
    right: 0;
    top: 404px;
    bottom: 0;
    background: var(--forest-green);
  }
  .contact-list {
    position: absolute;
    left: 40px;
    top: 190px;
    margin: 0;
    padding: 0;
    list-style: none;
  }
  .contact-list__item {
    display: flex;
    align-items: center;
    height: 36px;
    margin-bottom: 3px;
    font-family: "Tinos", "Times New Roman", serif;
    font-size: 21px;
    color: var(--ink);
  }
  .contact-icon {
    width: 28px;
    height: 28px;
    margin-right: 18px;
    flex: none;
  }
</style>
</head>
<body>
  <div class="business-card">
    <div class="identity">
      <h1 class="identity__name">YOUR NAME</h1>
      <p class="identity__title">xxxxx xxxxxx</p>
    </div>

    <div class="sprouting-coconut" role="img" aria-label="Photo of a sprouting coconut with green shoots"></div>

    <ul class="contact-list">
      <li class="contact-list__item">
        <svg class="contact-icon" viewBox="0 0 28 28" aria-hidden="true">
          <rect x="1" y="1" width="26" height="26" rx="4" fill="none" stroke="var(--icon)" stroke-width="2"/>
          <path d="M9 6c-1.5 0-3 1.5-2.5 3.5 1 5 6 10.5 11.5 12 2 .5 3.5-1 3.5-2.5l-3-2.5-2.2 1.5c-2-1-4-3-5-5l1.5-2.2z" fill="var(--icon)"/>
        </svg>
        000-0000-0000
      </li>
      <li class="contact-list__item">
        <svg class="contact-icon" viewBox="0 0 28 28" aria-hidden="true">
          <rect x="1" y="1" width="26" height="26" rx="4" fill="none" stroke="var(--icon)" stroke-width="2"/>
          <text x="14" y="18" text-anchor="middle" font-family="Arimo, Arial, sans-serif" font-size="9" font-weight="700" fill="var(--icon)">ABN</text>
        </svg>
        xxxxxxxxx
      </li>
      <li class="contact-list__item">
        <svg class="contact-icon" viewBox="0 0 28 28" aria-hidden="true">
          <rect x="1" y="1" width="26" height="26" rx="4" fill="none" stroke="var(--icon)" stroke-width="2"/>
          <circle cx="14" cy="14" r="7" fill="var(--icon)"/>
        </svg>
        xxxxxxxxxxxxxxxxxx
      </li>
      <li class="contact-list__item">
        <svg class="contact-icon" viewBox="0 0 28 28" aria-hidden="true">
          <rect x="1" y="1" width="26" height="26" rx="4" fill="none" stroke="var(--icon)" stroke-width="2"/>
          <path d="M6 14l16-7-5 15-3-6z" fill="var(--icon)"/>
        </svg>
        xxxxxxxxxxxx@tidemail.com
      </li>
      <li class="contact-list__item">
        <svg class="contact-icon" viewBox="0 0 28 28" aria-hidden="true">
          <rect x="1" y="1" width="26" height="26" rx="4" fill="none" stroke="var(--icon)" stroke-width="2"/>
          <rect x="8" y="8" width="12" height="12" fill="var(--icon)"/>
        </svg>
        xxxxxxx, xxxxx
      </li>
    </ul>

    <div class="accent-line"></div>
    <div class="footer-band"></div>
  </div>
</body>
</html>
```